Redesign My Travel Voucher Coupons-Please redesign the flyers I have attached to this brief.

These designs will be catered towards like travel agency vacation stays...luxury resort stays, hotel and airfare getaways, etc. so must have a travel theme but more importantly professional trustworthy appeal...

Please redesign the flyers I have attached to this brief.

I have attached my existing designs. Please use all existing content and elements exactly but make the design much better...also, please keep in mind that these would be full color and printer friendly...

Target Market(s)

Consumers. People receive these vouchers from businesses that run marketing promotions and contests and giveaways. So the look and feel must feel professional and trustworthy but not cheesy and fake.

Industry/Entity Type

Hotel

Requirements
Must have
• Please use all existing content and elements exactly but make the design much better...also, please keep in mind that these would be full color and printer friendly...

MUST HAVE ALL EXISTING CONTENT EXACT NO EXCEPTIONS
Nice to have
• These designs will be catered towards like travel agency vacation stays...luxury resort stays, hotel and airfare getaways, etc. so must have a travel theme but more importantly professional trustworthy appeal...

Should not have

```html
<!DOCTYPE html>
<html lang="en">
<head>
<meta charset="utf-8">
<title>4 Night Luxury Cruise Certificate</title>
<link href="https://fonts.googleapis.com/css2?family=Poppins:wght@200;300;400;500;600&display=swap" rel="stylesheet">
<style>
  :root{
    --backdrop:#c9c9c9;
    --paper:#f4f4f4;
    --ink:#2b2b2d;
    --body:#4a4a4c;
    --red:#a8101a;
    --red-soft:#d98a8f;
    --band:#e4e4e6;
    --bubble:#e3e3e5;
    --ticket:#e9e9eb;
    --dash:#8d8d90;
  }
  *{margin:0;padding:0;box-sizing:border-box}
  html,body{width:1070px;height:1200px;overflow:hidden;background:var(--backdrop)}
  body{font-family:"Poppins",sans-serif;color:var(--ink);position:relative}
  .page{position:absolute;left:81px;top:2px;width:825px;height:1088px;background:var(--paper);transform:scale(1.1);transform-origin:0 0}
  .abs{position:absolute}

  .side-band{left:31px;top:32px;width:44px;height:1035px;background:var(--band)}
  .side-photo{left:57px;top:49px;width:88px;height:998px;
    background:linear-gradient(180deg,#9fb0c4 0%,#6f7f9c 18%,#3f4f73 34%,#2c3551 48%,#3a3a44 62%,#5b5650 78%,#304560 88%,#1d2b45 100%)}

  .headline{left:168px;top:8px;font-weight:200;font-size:214px;line-height:1;letter-spacing:8px;color:var(--ink)}
  .title-bar{left:176px;top:210px;width:596px;height:33px;background:var(--red);color:#fff;font-weight:300;font-size:20px;text-align:center;line-height:33px;letter-spacing:.3px}
  .title-rule{left:170px;top:245px;width:600px;height:5px;background:var(--band)}

  .section-head{font-weight:300;font-size:21px;color:var(--red);letter-spacing:.5px}
  .copy{font-weight:300;font-size:10px;line-height:13.8px;color:var(--body)}

  .how-head{left:186px;top:288px}
  .how-copy{left:186px;top:330px;width:342px}
  .others-head{left:186px;top:456px}
  .quote{left:178px;top:490px;width:337px;height:75px;background:var(--bubble);border-radius:12px;padding:7px 12px}
  .quote-tail{left:222px;top:564px}
  .quote-author{left:186px;top:593px;font-weight:500;font-size:10.5px;color:var(--red)}

  .features-head{left:566px;top:288px}
  .feature-list{left:565px;top:329px;width:215px;list-style:none}
  .feature-list li{position:relative;padding-left:14px;font-weight:300;font-size:10px;line-height:12.5px;color:var(--body)}
  .feature-list svg{position:absolute;left:0;top:1px}

  .gateway{left:178px;top:655px;width:575px;text-align:center;font-weight:400;font-size:31px;letter-spacing:1.2px;color:var(--red)}
  .dash-rule{left:178px;width:575px;border-top:1px dashed var(--red-soft)}
  .recipient{left:178px;top:716px;width:575px;display:flex;justify-content:center;align-items:center;gap:26px;font-weight:300;font-size:22px;color:var(--ink)}
  .congrats{left:178px;top:776px;width:575px;text-align:center;font-weight:500;font-size:12px;line-height:14px;color:var(--ink)}
  .itinerary{left:190px;top:830px;width:551px;text-align:center;font-weight:300;font-size:10.5px;line-height:14px;color:var(--body)}

  .ticket{left:175px;top:904px;width:597px;height:94px}
  .ticket-info{left:214px;top:920px;font-size:10px;line-height:12px;color:var(--body);font-weight:300}
  .ticket-info b{display:block;color:var(--red);font-weight:500}
  .ticket-divider{left:311px;width:1px;height:24px;background:var(--body)}
  .ticket-offer{left:329px;top:920px;width:260px;font-weight:300;font-size:10px;line-height:12px;color:var(--body)}
  .ticket-url{left:328px;top:956px;font-weight:500;font-size:10.5px;color:var(--red)}
  .ticket-terms{left:327px;top:970px;font-weight:300;font-size:7px;color:var(--body)}

  .compliments{left:214px;top:1018px;display:flex;align-items:center;gap:16px;font-weight:300;font-size:13px;color:var(--ink)}
  .compliments .company{font-weight:400}
</style>
</head>
<body>
<main class="page">
  <div class="abs side-band"></div>
  <div class="abs side-photo" role="img" aria-label="Photo of a large cruise ship at dusk with lit decks above the sea"></div>

  <h1 class="abs headline">ENJOY</h1>
  <div class="abs title-bar">A 4 Night Luxury Cruise</div>
  <div class="abs title-rule"></div>

  <h2 class="abs section-head how-head">HOW CAN WE DO THIS?</h2>
  <p class="abs copy how-copy">We contract with world leading cruise lines to help them fill their otherwise empty rooms. The cruise lines now gain a new customer for their in-house restaurants, room service, the casino, spa and even future bookings. They know that if they show you a good time, you will probably tell your friends and family about the great time you had and may even book with them on a future cruise, but this time as a regular paying customer.</p>

  <h2 class="abs section-head others-head">WHAT OTHERS SAY?</h2>
  <blockquote class="abs quote copy">"The food was delicious in the buffet and the restaurant that was included in our ticket had delicious appetizers, entrees and desserts to choose from. The room was very clean and everything worked fine."</blockquote>
  <svg class="abs quote-tail" width="26" height="18" viewBox="0 0 26 18"><path d="M0 0H26L4 18Z" fill="var(--bubble)"/></svg>
  <p class="abs quote-author">Renata M. New York, NY</p>

  <h2 class="abs section-head features-head">FEATURES</h2>
  <ul class="abs feature-list">
    <li style="margin-bottom:18px"><svg width="9" height="9" viewBox="0 0 9 9"><circle cx="4.5" cy="4.5" r="3.8" fill="none" stroke="var(--red)" stroke-width="1"/><path d="M2.6 4.6l1.4 1.3 2.6-2.8" fill="none" stroke="var(--red)" stroke-width="1"/></svg>Phone Bookings With A Live Agent</li>
    <li style="margin-bottom:17px"><svg width="9" height="9" viewBox="0 0 9 9"><circle cx="4.5" cy="4.5" r="3.8" fill="none" stroke="var(--red)" stroke-width="1"/><path d="M2.6 4.6l1.4 1.3 2.6-2.8" fill="none" stroke="var(--red)" stroke-width="1"/></svg>Sail To: Cozumel, Nassau Bahamas or Ensenada</li>
    <li style="margin-bottom:18px"><svg width="9" height="9" viewBox="0 0 9 9"><circle cx="4.5" cy="4.5" r="3.8" fill="none" stroke="var(--red)" stroke-width="1"/><path d="M2.6 4.6l1.4 1.3 2.6-2.8" fill="none" stroke="var(--red)" stroke-width="1"/></svg>Sailing From: Miami, Port Canaveral or Los Angeles</li>
    <li style="margin-bottom:18px"><svg width="9" height="9" viewBox="0 0 9 9"><circle cx="4.5" cy="4.5" r="3.8" fill="none" stroke="var(--red)" stroke-width="1"/><path d="M2.6 4.6l1.4 1.3 2.6-2.8" fill="none" stroke="var(--red)" stroke-width="1"/></svg>Pay Just Taxes &amp; Fees</li>
    <li style="margin-bottom:18px"><svg width="9" height="9" viewBox="0 0 9 9"><circle cx="4.5" cy="4.5" r="3.8" fill="none" stroke="var(--red)" stroke-width="1"/><path d="M2.6 4.6l1.4 1.3 2.6-2.8" fill="none" stroke="var(--red)" stroke-width="1"/></svg>Fully Transferable To Another Person</li>
    <li style="margin-bottom:18px"><svg width="9" height="9" viewBox="0 0 9 9"><circle cx="4.5" cy="4.5" r="3.8" fill="none" stroke="var(--red)" stroke-width="1"/><path d="M2.6 4.6l1.4 1.3 2.6-2.8" fill="none" stroke="var(--red)" stroke-width="1"/></svg>Redeem Now, Travel Later</li>
    <li style="margin-bottom:17px"><svg width="9" height="9" viewBox="0 0 9 9"><circle cx="4.5" cy="4.5" r="3.8" fill="none" stroke="var(--red)" stroke-width="1"/><path d="M2.6 4.6l1.4 1.3 2.6-2.8" fill="none" stroke="var(--red)" stroke-width="1"/></svg>You Will Have 24 Months To Complete Travel Offer</li>
    <li><svg width="9" height="9" viewBox="0 0 9 9"><circle cx="4.5" cy="4.5" r="3.8" fill="none" stroke="var(--red)" stroke-width="1"/><path d="M2.6 4.6l1.4 1.3 2.6-2.8" fill="none" stroke="var(--red)" stroke-width="1"/></svg>No Timeshare Or Sales Presentations, Guaranteed!</li>
  </ul>

  <h2 class="abs gateway">A 4 Night Luxuxy Cruise Gateway</h2>
  <div class="abs dash-rule" style="top:707px"></div>
  <div class="abs recipient">
    <span>EXCLUSIVELY FOR</span>
    <svg width="24" height="12" viewBox="0 0 24 12"><path d="M1 1l5 5-5 5M9 1l5 5-5 5M17 1l5 5-5 5" fill="none" stroke="var(--red)" stroke-width="1.4"/></svg>
    <span>MARCUS ELLERY</span>
  </div>
  <div class="abs dash-rule" style="top:755px"></div>

  <p class="abs congrats">Congratulations, you are the lucky recipient of a 5 day /4 night Cruise<br>aboard choice of: Harborline Cruises, Coral Crown Voyages, Northwind Sea Lines,<br>or Duchess Cruises.</p>
  <p class="abs itinerary">There are 3 itineraries w/ ports of departure including: Miami to Cozumel, Port Canaveral to Nassau, or LA to Ensenada, Mexico. All cruises include unlimited access to the on-board buffets for breakfast, lunch and dinner. Vegas style entertainment and use of all on-board facilities. You simply pay taxes and port fees. Have the time of your life while enjoying the luxuries of a cruise vacation!</p>

  <svg class="abs ticket" viewBox="0 0 597 94" role="img" aria-label="Redemption ticket with a photo of a cruise ship at sea">
    <defs>
      <clipPath id="ticket-shape"><path d="M14 0H583q0 14 14 14V80q-14 0-14 14H14q0-14-14-14V14q14 0 14-14Z"/></clipPath>
      <linearGradient id="sea-sky" x1="0" y1="0" x2="0" y2="1">
        <stop offset="0" stop-color="#6d97bf"/><stop offset=".55" stop-color="#b9cfe0"/><stop offset=".62" stop-color="#2f6a93"/><stop offset="1" stop-color="#1d4c72"/>
      </linearGradient>
    </defs>
    <g clip-path="url(#ticket-shape)">
      <rect width="597" height="94" fill="var(--ticket)"/>
      <path d="M398 0H597V94H412Z" fill="url(#sea-sky)"/>
    </g>
    <path d="M18 5H579q2 12 13 13V76q-11 1-13 13H18q-2-12-13-13V18q11-1 13-13Z" fill="none" stroke="var(--dash)" stroke-width="1" stroke-dasharray="3 2"/>
  </svg>
  <div class="abs ticket-info">CERTIFICATE ID<b>91772-11222</b></div>
  <div class="abs ticket-info" style="top:956px">EXPIRES<b>10/17/2020</b></div>
  <div class="abs ticket-divider" style="top:920px"></div>
  <div class="abs ticket-divider" style="top:956px"></div>
  <p class="abs ticket-offer">VIEW ALL THE DETAILS OF THIS SPECIAL<br>OFFER AND REDEEM ONLINE AT</p>
  <p class="abs ticket-url">WWW.VOYAGEREWARDSDESK.COM</p>
  <p class="abs ticket-terms">*TERMS AND CONDITIONS APPLY SEE WEBSITE FOR DETAILS</p>

  <div class="abs compliments">
    <span>THIS CERTIFICATE IS COMPLIMENTS OF</span>
    <svg width="24" height="12" viewBox="0 0 24 12"><path d="M1 1l5 5-5 5M9 1l5 5-5 5M17 1l5 5-5 5" fill="none" stroke="var(--red)" stroke-width="1.4"/></svg>
    <span class="company">Your Company Name Here</span>
  </div>
</main>
</body>
</html>
```